Professional Business Cards for Recruiting Company

We'd like professional 2-sided business cards that reflect a color scheme that matches our website, www.queryvantline.com, and / or logo that is attached.

Slogan used is "We Know People", but needs to be editable because we change it up to "We Know Developers", "We Speak Geek", etc.

Must includes logo, slogan, first and last name, address, email, mobile number and website address.

Files attached for ideas.

Thanks!

Contact Information for Business Card

Logo, Company name, First name, Last name, addresss, email, phone, website address.

Font styles to use
Sans Serif

Colors
0054AA
0677BA
7BADD7
CADEEF
E8F1F8

Requirements
Nice to have
• I do like the following designs. 22962062 and 22962651. Couple ideas anyway.

```html
<!DOCTYPE html>
<html lang="en">
<head>
<meta charset="utf-8">
<title>Queryvantline Business Card</title>
<link rel="stylesheet" href="https://fonts.googleapis.com/css2?family=Montserrat:wght@400;800&family=Raleway:wght@300;400;700&display=swap">
<style>
  :root {
    --brand-blue: #1e4f8a;
    --ink-grey: #6b6b6b;
    --ink-dark: #2f2f2f;
    --paper: #ffffff;
    --backdrop: #e6e7e9;
  }
  * { margin: 0; padding: 0; box-sizing: border-box; }
  html, body { width: 1003px; height: 1200px; overflow: hidden; }
  body { background: var(--backdrop); position: relative; font-family: "Raleway", sans-serif; }

  .card { position: absolute; left: 75px; width: 853px; height: 487px; overflow: hidden; }
  .card-front { top: 74px; background: var(--paper); }
  .card-back { top: 608px; height: 491px; background: var(--brand-blue); }

  .brand-square { position: absolute; left: 196px; top: 96px; width: 72px; height: 72px; background: var(--brand-blue); }
  .brand-name { position: absolute; left: 310px; top: 96px; width: 412px; font-family: "Raleway", sans-serif; font-weight: 300; font-size: 46px; line-height: 58px; color: var(--brand-blue); white-space: nowrap; }
  .brand-rule { position: absolute; left: 313px; top: 156px; width: 408px; height: 2px; background: var(--brand-blue); }
  .brand-tagline { position: absolute; left: 313px; top: 164px; width: 408px; font-family: "Montserrat", sans-serif; font-weight: 800; font-size: 13px; line-height: 16px; letter-spacing: 2.1px; color: var(--ink-grey); white-space: nowrap; }

  .person { position: absolute; right: 437px; top: 268px; text-align: right; }
  .person-name { font-family: "Montserrat", sans-serif; font-weight: 800; font-size: 31px; letter-spacing: -0.5px; color: var(--brand-blue); line-height: 38px; }
  .person-title { font-family: "Raleway", sans-serif; font-weight: 400; font-size: 23px; color: var(--ink-dark); line-height: 30px; margin-top: 1px; letter-spacing: 0.3px; }

  .divider { position: absolute; left: 443px; top: 259px; width: 2px; height: 83px; background: var(--ink-dark); }

  .contacts { position: absolute; left: 466px; top: 253px; list-style: none; }
  .contact { display: flex; align-items: center; height: 34px; font-size: 22px; color: var(--ink-dark); white-space: nowrap; }
  .contact svg { width: 20px; height: 20px; margin-right: 15px; flex: none; }

  .address-band { position: absolute; left: 0; top: 387px; width: 100%; height: 36px; background: var(--brand-blue); color: var(--paper); text-align: center; font-size: 22px; line-height: 36px; letter-spacing: 0.3px; }

  .back-mark { position: absolute; left: 0; top: 186px; width: 100%; text-align: center; font-family: "Raleway", sans-serif; font-weight: 700; font-size: 52px; color: var(--paper); letter-spacing: 1px; }
  .slogan { position: absolute; left: 0; top: 400px; width: 100%; text-align: center; font-family: "Montserrat", sans-serif; font-weight: 400; font-size: 31px; letter-spacing: 4.5px; color: var(--paper); }
</style>
</head>
<body>
  <section class="card card-front">
    <div class="brand-square"></div>
    <div class="brand-name">QUERYVANTLINE</div>
    <div class="brand-rule"></div>
    <div class="brand-tagline">PROFESSIONAL SOURCING AND RECRUITING</div>

    <div class="person">
      <div class="person-name">MARCUS DELANEY</div>
      <div class="person-title">Managing Director</div>
    </div>

    <div class="divider"></div>

    <ul class="contacts">
      <li class="contact">
        <svg viewBox="0 0 24 24" aria-hidden="true"><path fill="#1e4f8a" d="M6.6 10.8c1.4 2.8 3.8 5.1 6.6 6.6l2.2-2.2c.3-.3.7-.4 1-.2 1.1.4 2.3.6 3.6.6.6 0 1 .4 1 1V20c0 .6-.4 1-1 1C10.6 21 3 13.4 3 4c0-.6.4-1 1-1h3.5c.6 0 1 .4 1 1 0 1.3.2 2.5.6 3.6.1.3 0 .7-.2 1z"/><path fill="none" stroke="#1e4f8a" stroke-width="1.6" d="M14 3.5a7 7 0 0 1 6.5 6.5M14 7a3.5 3.5 0 0 1 3 3"/></svg>
        044-318 672 905
      </li>
      <li class="contact">
        <svg viewBox="0 0 24 24" aria-hidden="true"><rect x="2" y="5" width="20" height="14" fill="#1e4f8a"/><path d="M2.5 5.5 12 13l9.5-7.5M2.5 18.5l7-6M21.5 18.5l-7-6" fill="none" stroke="#fff" stroke-width="1.3"/></svg>
        hello@queryvantline.com
      </li>
      <li class="contact">
        <svg viewBox="0 0 24 24" aria-hidden="true"><circle cx="12" cy="12" r="10" fill="#1e4f8a"/><path fill="#fff" d="M7 6c2 0 3 1 3 2.5S8 10 8.5 11.5 11 13 10.5 15 9 17 8 19c-2-1.5-4-4-4-7 0-2.5 1.2-4.6 3-6zM15 5.5c1 .5 2 1.5 1.5 2.5S14 8 14 9.5s2 1.5 3.5 1.5 2.5 1 2.5 2.5c-.5 2-1.5 3.5-3 4.5-.5-1.5-1-3-2.5-3.5S12 12 12.5 10.5 14 8 15 5.5z"/></svg>
        www.queryvantline.com
      </li>
    </ul>

    <div class="address-band">87, Harbor Row&nbsp; Easton Vale, 30718</div>
  </section>

  <section class="card card-back">
    <div class="back-mark">QUERYVANTLINE</div>
    <div class="slogan">We Know Developers</div>
  </section>
</body>
</html>
```